One page responsive Wordpress Website

I am looking to design and code for 1-page Wordpress responsive website (desktop/mobile/tablet). Pls see attached file. Job scope includes Wordpress design and coding of the actual Live website
Target Market(s)
Small medium business
Industry/Entity Type
Telecommunications
Font styles to use
Sans Serif
Colors
ffffff
85cae6
63bae0
33a6d7
cedeed
3277b5
Requirements
Must have
- One page only, Wordpress, Responsive layout in desktop, mobile, tablet

```html
<!DOCTYPE html>
<html lang="en">
<head>
<meta charset="utf-8">
<title>Calvion IP Phone</title>
<link rel="stylesheet" href="https://fonts.googleapis.com/css2?family=Montserrat:wght@300;400;500;600;700;800&display=swap">
<style>
:root{
  --white:#ffffff;
  --sky:#85cae6;
  --sky-mid:#63bae0;
  --brand:#33a6d7;
  --mist:#cedeed;
  --deep:#3277b5;
  --ink:#1d1d1d;
  --text:#4a4a4a;
  --pale:#eef4fa;
  --field-line:#e4e8ec;
  --submit:#14a4ea;
}
*{box-sizing:border-box;margin:0;padding:0}
html,body{width:1200px;height:2556px;overflow:hidden}
body{font-family:"Montserrat",sans-serif;color:var(--ink);background:var(--white);position:relative}
.abs{position:absolute}

/* header */
.site-header{position:absolute;left:0;top:0;width:1200px;height:82px;background:var(--white)}
.brand-name{position:absolute;left:163px;top:16px;font-size:40px;font-weight:700;color:var(--brand);letter-spacing:.5px}
.nav-btn{position:absolute;top:25px;height:36px;border:1px solid #3a4a5a;font-size:14px;display:flex;align-items:center;justify-content:center;color:var(--ink)}
.nav-about{left:829px;width:95px}
.nav-contact{left:942px;width:96px}

/* hero */
.hero{position:absolute;left:0;top:82px;width:1200px;height:512px;background:linear-gradient(90deg,#4b5257 0%,#6f777c 35%,#b8b9b5 60%,#dcdcd8 100%)}
.hero-kicker{position:absolute;left:163px;top:206px;font-size:20px;font-weight:700;color:var(--white);text-shadow:0 1px 3px rgba(0,0,0,.5)}
.hero-title{position:absolute;left:163px;top:240px;font-size:42px;font-weight:700;color:var(--white);text-shadow:0 1px 3px rgba(0,0,0,.5)}
.hero-text{position:absolute;left:163px;top:304px;width:410px;font-size:16.5px;line-height:25px;font-weight:600;color:var(--white);text-shadow:0 1px 3px rgba(0,0,0,.5)}

/* products */
.section-title{position:absolute;left:0;width:1200px;text-align:center;font-weight:800}
.products-title{top:664px;font-size:42px}
.product{position:absolute;top:752px;width:300px;text-align:center}
.product-name{font-size:21px;font-weight:500;color:var(--brand)}
.product-shot{margin:14px auto 0;width:210px;height:260px;background:linear-gradient(160deg,#5a6573,#2e3742);border-radius:8px}
.product-shot.tall{width:160px;height:272px;background:linear-gradient(180deg,#3a4556,#202a3a)}
.features{display:flex;justify-content:center;gap:8px;margin-top:12px;height:34px}
.feature{width:34px;height:34px;background:var(--mist);border-radius:3px;display:flex;align-items:center;justify-content:center}
.download{position:absolute;left:30px;top:366px;width:240px;height:45px;border:1px solid var(--brand);display:flex;align-items:center;justify-content:center;gap:10px;font-size:14px;font-weight:600;color:var(--brand)}

/* about */
.about{position:absolute;left:0;top:1240px;width:1200px;height:433px;background:linear-gradient(180deg,#e9f1f8,#f6f9fc)}
.about-title{position:absolute;left:163px;top:75px;font-size:38px;font-weight:700;color:var(--deep)}
.about-title span{color:var(--brand)}
.about-rule{position:absolute;left:163px;top:124px;width:61px;height:2px;background:var(--brand)}
.about-text{position:absolute;left:163px;top:137px;width:488px;font-size:15.5px;line-height:27px;font-weight:400;color:var(--text);text-align:justify;letter-spacing:.3px}
.ring{position:absolute;border-radius:50%;border:1.5px solid var(--sky)}
.about-photo{position:absolute;left:773px;top:100px;width:228px;height:228px;border-radius:50%;background:radial-gradient(circle at 50% 40%,#f4f4f2,#c9c7c0 70%,#9c9a94)}
.strip{position:absolute;left:0;top:1673px;width:1200px;height:20px;background:#f1f3f5}

/* contact */
.contact-title{top:1764px;font-size:34px;color:#2c2c2c;font-weight:700}
.contact-rule{position:absolute;left:581px;top:1816px;width:37px;height:3px;background:var(--brand)}
.contact-lead{position:absolute;left:0;width:1200px;text-align:center;font-size:14.5px;color:#333;line-height:19px}
.field{position:absolute;height:46px;background:var(--white);box-shadow:0 1px 6px rgba(0,0,0,.08);display:flex;align-items:center;font-size:12.5px;color:#333}
.field .icon{width:39px;height:34px;border-right:1px solid var(--field-line);display:flex;align-items:center;justify-content:center;margin-right:14px}
.field.area{height:89px;align-items:flex-start;padding-top:12px}
.submit{position:absolute;left:554px;top:2154px;width:92px;height:36px;border-radius:18px;background:var(--submit);color:var(--white);font-size:13px;font-weight:600;display:flex;align-items:center;justify-content:center}

/* footer */
.footer{position:absolute;left:0;top:2220px;width:1200px;height:304px;background:linear-gradient(180deg,#f0f1f3,#dfe2e5 60%,#d3d7db)}
.footer-brand{position:absolute;left:0;top:56px;width:1200px;text-align:center;font-size:40px;font-weight:700;color:var(--brand)}
.footer-tag{position:absolute;left:0;top:116px;width:1200px;text-align:center;font-size:21px;font-weight:500;color:var(--ink)}
.info{position:absolute;top:192px;display:flex;gap:14px;font-size:15px;line-height:23px;color:var(--ink)}
.info .dot{width:40px;height:40px;border-radius:50%;background:var(--sky);display:flex;align-items:center;justify-content:center;margin-top:2px;flex:none}
.divider{position:absolute;top:195px;width:0;height:48px;border-left:1px dashed #9aa2aa}
.bottom-bar{position:absolute;left:0;top:2524px;width:1200px;height:32px;background:var(--brand);color:var(--white);font-size:12px}
.bottom-bar .copy{position:absolute;left:163px;top:9px;font-weight:300}
.bottom-bar .links{position:absolute;right:163px;top:9px;font-weight:500}
</style>
</head>
<body>

<header class="site-header">
  <div class="brand-name">Calvion</div>
  <div class="nav-btn nav-about">About Us</div>
  <div class="nav-btn nav-contact">Contact Us</div>
</header>

<section class="hero" role="img" aria-label="Bright modern office with a desk IP phone on a white table beside a printer">
  <div class="hero-kicker">Enterprise HD IP Phone</div>
  <div class="hero-title">Calvion IP Phone</div>
  <p class="hero-text">The Most Affordable IP Phone, With Highest Compatibility To Every IP-PBX System. Sleek Designed And User-friendly Proven.</p>
</section>

<h2 class="section-title products-title">Our Products</h2>

<div class="product" style="left:152px">
  <div class="product-name">Calvion CX310G</div>
  <div class="product-shot" role="img" aria-label="Grey desk IP phone with colour screen and handset"></div>
  <div class="features">
    <div class="feature"></div><div class="feature"></div><div class="feature"></div><div class="feature"></div>
  </div>
  <div class="download">
    <svg width="20" height="20" viewBox="0 0 20 20" fill="none" stroke="currentColor" stroke-width="2"><path d="M10 2v11M5 8l5 5 5-5M2 14v4h16v-4"/></svg>
    Download Datasheet (EN)
  </div>
</div>

<div class="product" style="left:450px">
  <div class="product-name">Calvion CX520G</div>
  <div class="product-shot" role="img" aria-label="Grey desk IP phone with 2.8 inch screen and handset"></div>
  <div class="features">
    <div class="feature" style="font-size:8px;color:#333">1000M</div>
    <div class="feature" style="font-size:9px;font-weight:700;color:#333;line-height:9px;text-align:center">2.8<br>INCH</div>
    <div class="feature"></div><div class="feature"></div><div class="feature"></div><div class="feature"></div>
  </div>
  <div class="download">
    <svg width="20" height="20" viewBox="0 0 20 20" fill="none" stroke="currentColor" stroke-width="2"><path d="M10 2v11M5 8l5 5 5-5M2 14v4h16v-4"/></svg>
    Download Datasheet (EN)
  </div>
</div>

<div class="product" style="left:748px">
  <div class="product-name">Calvion CX40</div>
  <div class="product-shot tall" role="img" aria-label="Dark expansion module with tall contact list display"></div>
  <div class="features"></div>
  <div class="download">
    <svg width="20" height="20" viewBox="0 0 20 20" fill="none" stroke="currentColor" stroke-width="2"><path d="M10 2v11M5 8l5 5 5-5M2 14v4h16v-4"/></svg>
    Download Datasheet (EN)
  </div>
</div>

<section class="about">
  <h2 class="about-title">About <span>Us</span></h2>
  <div class="about-rule"></div>
  <p class="about-text">Calvion IP Phones Is Designed With Pixel Colour LCD With Backlight LED, Built-in Gigabit Ethernet With Up To 28 Various Features. Equipped With Power Over Ethernet (PoE) Support, And High Definition (HD) Sound Quality With A Rich Visual Experience. Designed With A Fresh Appearance, It Supports Flexible And Secured Provisioning, Deliver Modern Elegant Appearance, Superb Sound Quality And A Rich Set Of IP/SIP Telephony Features.</p>
  <div class="ring" style="left:736px;top:62px;width:302px;height:302px"></div>
  <div class="ring" style="left:748px;top:74px;width:278px;height:278px;border-color:#b5dcee"></div>
  <div class="about-photo" role="img" aria-label="Black desk IP phone on a wooden table"></div>
</section>
<div class="strip"></div>

<h2 class="section-title contact-title">CONTACT US NOW</h2>
<div class="contact-rule"></div>
<p class="contact-lead" style="top:1834px">Speak To Us Or Send Us An Enquiry For Free Consultation</p>
<p class="contact-lead" style="top:1860px">Our team would love to share more about Calvion IP Phones. We are expecting your calls and<br>emails. Drop us an enquiry form at your fingertips!</p>

<div class="field" style="left:271px;top:1919px;width:344px">
  <div class="icon"><svg width="12" height="12" viewBox="0 0 12 12" fill="#aaa"><circle cx="6" cy="3.5" r="3"/><path d="M0 12c0-4 3-5 6-5s6 1 6 5z"/></svg></div>Your Name*
</div>
<div class="field" style="left:636px;top:1919px;width:345px">
  <div class="icon"><svg width="10" height="13" viewBox="0 0 10 13" fill="#aaa"><path d="M5 0a5 5 0 0 0-5 5c0 4 5 8 5 8s5-4 5-8a5 5 0 0 0-5-5zm0 7a2 2 0 1 1 0-4 2 2 0 0 1 0 4z"/></svg></div>Email*
</div>
<div class="field" style="left:271px;top:1978px;width:344px">
  <div class="icon"><svg width="12" height="12" viewBox="0 0 12 12" fill="#aaa"><path d="M2 0l2.5 3-1.5 1.5c.8 1.8 2.2 3.2 4 4L8.5 7 12 9.5 10 12C4.5 11.5.5 7.5 0 2z"/></svg></div>Phone*
</div>
<div class="field" style="left:636px;top:1978px;width:345px">
  <div class="icon"><svg width="13" height="13" viewBox="0 0 13 13" fill="none" stroke="#aaa" stroke-width="1.3"><path d="M9 1H1v11h11V5"/><path d="M5 8l1-3 6-4 1 1-4 6z"/></svg></div>Inquiry For*
</div>
<div class="field area" style="left:271px;top:2038px;width:710px">
  <div class="icon" style="height:34px;margin-top:-6px"><svg width="14" height="14" viewBox="0 0 14 14" fill="none" stroke="#aaa"><circle cx="7" cy="7" r="6.3"/><text x="7" y="10.5" font-size="9" text-anchor="middle" fill="#aaa" stroke="none" font-family="sans-serif">?</text></svg></div>How can we help you?
</div>
<div class="submit">SUBMIT</div>

<footer class="footer" role="img" aria-label="Faint city skyline with network connection lines">
  <div class="footer-brand">Calvion</div>
  <div class="footer-tag">Make A Better Connection For Your Business</div>
  <div class="info" style="left:161px">
    <div class="dot"><svg width="14" height="18" viewBox="0 0 10 13" fill="#fff"><path d="M5 0a5 5 0 0 0-5 5c0 4 5 8 5 8s5-4 5-8a5 5 0 0 0-5-5zm0 7a2 2 0 1 1 0-4 2 2 0 0 1 0 4z"/></svg></div>
    <div>123, Building Name, Street<br>City, State XY 123456</div>
  </div>
  <div class="divider" style="left:466px"></div>
  <div class="info" style="left:526px">
    <div class="dot"><svg width="18" height="18" viewBox="0 0 12 12" fill="#fff"><path d="M2 0l2.5 3-1.5 1.5c.8 1.8 2.2 3.2 4 4L8.5 7 12 9.5 10 12C4.5 11.5.5 7.5 0 2z"/></svg></div>
    <div>Phone<br>+1 555 014 2290</div>
  </div>
  <div class="divider" style="left:759px"></div>
  <div class="info" style="left:820px">
    <div class="dot"><svg width="18" height="18" viewBox="0 0 16 16" fill="#fff"><path d="M16 0L0 7l5 2 1 6 3-4 4 3z"/></svg></div>
    <div>Email<br>inquiry@calvion.com</div>
  </div>
</footer>

<div class="bottom-bar">
  <div class="copy">Copyright © 2021 Calvion. All Rights Reserved.</div>
  <div class="links">About Us &nbsp;&nbsp;|&nbsp;&nbsp; Contact Us</div>
</div>

</body>
</html>
```